Our Crooked Plot: Need a label for bee and garden related products

We want to distribute some homemade goods from our bees and greenhouse garden to friends, family, and neighbors. Things like honey, beeswax candles, lip balm, tomato sauce, pickles, etc. The yard itself is also a bit odd as it's almost an acre, but it's really long and narrow. We'd like to call it "Our Crooked Plot". We're open to a variety of designs and really don't have specific preferences just yet.

Font styles to use
Serif
Decorative
Script

Requirements
Must have
• The company name, Our Crooked Plot.

```html
<!DOCTYPE html>
<html lang="en">
<head>
<meta charset="utf-8">
<title>Our Crooked Plot — Product Labels</title>
<link rel="stylesheet" href="https://fonts.googleapis.com/css2?family=Yanone+Kaffeesatz:wght@300;400&display=swap">
<style>
  :root {
    --sky: #b3d5ee;
    --paper: #ffffff;
    --ink: #231815;
    --honey: #f6c500;
    --pattern: #8c8584;
    --shadow: rgba(40, 70, 100, 0.35);
  }
  * { margin: 0; padding: 0; box-sizing: border-box; }
  html, body { width: 1200px; height: 1200px; overflow: hidden; }
  body {
    background: var(--sky);
    position: relative;
    font-family: "Yanone Kaffeesatz", "Arial Narrow", sans-serif;
    color: var(--ink);
  }
  .abs { position: absolute; }
  .rule-solid { position: absolute; height: 3px; background: var(--ink); }
  .rule-dotted { position: absolute; height: 0; border-top: 1.5px dotted var(--ink); }
  .pattern-row { position: absolute; height: 5px; background: var(--pattern); border-radius: 3px; }
  .bee-mark {
    position: absolute; width: 13px; height: 13px;
    border: 2px solid var(--ink); border-radius: 50%;
    transform: translate(-50%, -50%);
  }
  .brand-name {
    position: absolute; left: 0; right: 0; text-align: center;
    font-weight: 300; line-height: 1; white-space: nowrap;
    transform: translateY(-50%);
  }
  .product-name {
    position: absolute; left: 0; right: 0; text-align: center;
    font-weight: 400; letter-spacing: 0.02em; line-height: 1;
    transform: translateY(-50%);
  }

  /* Round candle label */
  .candle-label { left: 408px; top: 68px; width: 384px; height: 384px; filter: drop-shadow(3px 4px 4px var(--shadow)); }
  .candle-label svg { position: absolute; inset: 0; }
  .candle-content { position: absolute; left: 0; top: 0; width: 1200px; height: 1200px; pointer-events: none; }

  /* Lip balm strip */
  .balm-label {
    left: 370px; top: 513px; width: 462px; height: 138px;
    background: var(--paper); box-shadow: 3px 4px 5px var(--shadow);
  }
  .balm-band { position: absolute; left: 0; right: 0; height: 2.5px; background: var(--honey); }

  /* Honey jar label */
  .honey-label {
    left: 362px; top: 710px; width: 478px; height: 384px;
    background: var(--paper); box-shadow: 3px 4px 5px var(--shadow);
  }
  .honey-band { position: absolute; left: 0; right: 0; height: 16px; background: var(--honey); }
  .honey-edge { position: absolute; left: 0; right: 0; height: 2.5px; background: var(--ink); }
</style>
</head>
<body>

  <!-- Beeswax candle: round label -->
  <div class="abs candle-label">
    <svg width="384" height="384" viewBox="0 0 384 384">
      <circle cx="192" cy="192" r="192" fill="var(--honey)"/>
      <circle cx="192" cy="192" r="178" fill="var(--paper)" stroke="var(--ink)" stroke-width="4"/>
      <circle cx="192" cy="192" r="157" fill="none" stroke="var(--pattern)" stroke-width="5" role="img" aria-label="Ring of small bee ornaments"/>
    </svg>
  </div>
  <div class="candle-content">
    <span class="bee-mark" style="left:600px; top:184px;"></span>
    <div class="rule-dotted" style="left:496px; top:208px; width:208px;"></div>
    <div class="rule-solid" style="left:496px; top:213px; width:208px;"></div>
    <div class="brand-name" style="top:254px; font-size:37px;">Our Crooked Plot</div>
    <div class="rule-solid" style="left:496px; top:299px; width:208px;"></div>
    <div class="pattern-row" role="img" aria-label="Row of small bee ornaments" style="left:496px; top:309px; width:208px;"></div>
    <div class="rule-dotted" style="left:496px; top:322px; width:208px;"></div>
    <div class="product-name" style="top:372px; font-size:12px;">BEESWAX CANDLE</div>
  </div>

  <!-- Lip balm: wrap strip -->
  <div class="abs balm-label">
    <span class="bee-mark" style="left:231px; top:21px; width:11px; height:11px;"></span>
    <div class="balm-band" style="top:38px;"></div>
    <div class="rule-solid" style="left:0; top:55px; width:132px; height:2px;"></div>
    <div class="pattern-row" role="img" aria-label="Row of small bee ornaments" style="left:4px; top:64px; width:128px; height:4px;"></div>
    <div class="rule-dotted" style="left:0; top:78px; width:132px;"></div>
    <div class="brand-name" style="top:67px; font-size:30px;">Our Crooked Plot</div>
    <div class="rule-solid" style="left:332px; top:55px; width:130px; height:2px;"></div>
    <div class="pattern-row" role="img" aria-label="Row of small bee ornaments" style="left:332px; top:64px; width:126px; height:4px;"></div>
    <div class="rule-dotted" style="left:332px; top:78px; width:130px;"></div>
    <div class="balm-band" style="top:93px;"></div>
    <div class="product-name" style="top:111px; font-size:11px;">LIP BALM</div>
  </div>

  <!-- Honey: jar label -->
  <div class="abs honey-label">
    <div class="honey-band" style="top:0;"></div>
    <div class="honey-edge" style="top:17px;"></div>
    <div class="pattern-row" role="img" aria-label="Row of small bee ornaments" style="left:10px; right:10px; top:30px;"></div>
    <span class="bee-mark" style="left:239px; top:95px; width:15px; height:15px;"></span>
    <div class="rule-dotted" style="left:100px; top:114px; width:277px;"></div>
    <div class="rule-solid" style="left:100px; top:123px; width:277px;"></div>
    <div class="brand-name" style="top:178px; font-size:46px;">Our Crooked Plot</div>
    <div class="rule-solid" style="left:100px; top:236px; width:277px;"></div>
    <div class="pattern-row" role="img" aria-label="Row of small bee ornaments" style="left:100px; top:251px; width:277px;"></div>
    <div class="rule-dotted" style="left:100px; top:268px; width:277px;"></div>
    <div class="product-name" style="top:308px; font-size:17px;">HONEY</div>
    <div class="pattern-row" role="img" aria-label="Row of small bee ornaments" style="left:10px; right:10px; top:349px;"></div>
    <div class="honey-edge" style="top:365px;"></div>
    <div class="honey-band" style="top:368px;"></div>
  </div>

</body>
</html>
```